Scrubbing Paper Towel Company needs Label Design

We need a product label that wraps around a roll of scrubbing paper towels as a sticker label of individually wrapped rolls. The sticker label has dimensions of 11.5" x 6" (width x height). The company logo with the brand feel and color theme is attached.

This is mainly used for dishwashing. A very large section of the label should show dishwashing and cleaning. Two very similar products can be found here :
---> https://www.shopvarnel.example/Non-Scratch-Disposable-Dish-Washing-Scrubbing-KT47M/dp/Q5283LRTVN/ref=sr_1_9?keywords=scouring+sheet&qid=2840175396&sr=8-9
--->https://www.shopvarnel.example/Zuvi-Flair-Disposable-Dish-washing-Scrubbing/dp/Q3961HWPXT/ref=sr_1_15?keywords=scouring+sheet&qid=2840175396&sr=8-15

To be included in the label:

Key points:
Did you know? Sponges are the perfect place for bacteria growth! We're talking hundreds of different species of bacteria growing in your dishwashing sponge - just as bad as the inside of your toilet. So why use a dirty sponge over and over again? Why does it smell so bad? Yes your toilet is gross, but why should the sponge go overlooked?

The Brisko Roll is a sanitary solution to this problem. Use it once, wash and reuse up to three times before throwing each sheet away - that's enough for 180 washes per roll! But don't limit yourself to dishwashing. It's great for scrubbing surfaces with hardened debris or even dry residue left from old spills. So go ahead, take a stand against bacteria and wash away knowing your kitchen is finally clean. Now that's sanitary!

Multipurpose Use:
Dishwashing
**(with example image/graphic)**
Cleaning Toilets
Cleaning Grills
Wiping Down Stoves
Cleaning Sinks
Cleaning Pet Bowls

60 Sheets
7.9" X 8.7" per sheet

Features:
Perforated for Easy Tear
Reusable
Liquid Absorbent
Non-Flammable
Cadmium Free
Kitchen Safe

```html
<!DOCTYPE html>
<html lang="en">
<head>
<meta charset="utf-8">
<title>Brisko Roll – Roll Label</title>
<link href="https://fonts.googleapis.com/css2?family=Roboto:ital,wght@0,300;0,400;0,700;1,700;1,900&family=Roboto+Condensed:ital,wght@1,700&display=swap" rel="stylesheet">
<style>
  :root{
    --navy-deep:#0c1a52;
    --navy:#16297a;
    --royal:#1f3aa0;
    --sky:#4aa6dc;
    --sky-dot:#4b9fd6;
    --white:#ffffff;
    --ice:#e8eef8;
    --ring:#2446b0;
  }
  *{margin:0;padding:0;box-sizing:border-box}
  html,body{width:1200px;height:626px;overflow:hidden;background:var(--navy-deep)}
  .label{
    position:relative;width:1200px;height:626px;overflow:hidden;
    background:
      radial-gradient(ellipse 70% 90% at 25% 35%, var(--royal) 0%, var(--navy) 55%, var(--navy-deep) 100%);
    font-family:"Roboto",Arial,sans-serif;color:var(--white);
  }
  .swoosh{position:absolute;left:0;top:0;width:1200px;height:626px}
  .brand{
    position:absolute;left:95px;top:150px;width:340px;
    display:flex;align-items:center;gap:14px;
  }
  .brand-mark{width:22px;height:22px;border-radius:50%;background:var(--white);flex:none}
  .brand-name{font-weight:900;font-size:56px;line-height:1;letter-spacing:-1px;color:var(--white)}

  .features{list-style:none}
  .feature{
    position:absolute;font-weight:700;font-style:italic;font-size:19px;
    white-space:nowrap;text-shadow:0 1px 3px rgba(0,0,0,.45);
    transform:translateY(-50%);
  }
  .feature::after{
    content:"";position:absolute;top:50%;width:15px;height:15px;border-radius:50%;
    background:var(--sky-dot);transform:translateY(-50%);
  }
  .f1{right:513px;top:117px}.f1::after{right:-33px}
  .f2{right:525px;top:169px}.f2::after{right:-33px}
  .f3{right:530px;top:221px}.f3::after{right:-38px}
  .f4{right:540px;top:273px}.f4::after{right:-40px}
  .f5{right:567px;top:325px}.f5::after{right:-40px}
  .f6{right:603px;top:377px}.f6::after{right:-51px}

  .facts-title{
    position:absolute;left:806px;top:80px;
    font-family:"Roboto Condensed",Arial,sans-serif;font-weight:700;font-style:italic;font-size:24px;
  }
  .facts p{font-weight:300;font-size:16px}
  .line{position:absolute;right:35px;white-space:nowrap;line-height:23px}
  .j{text-align:justify;text-align-last:justify}

  .uses-tab{
    position:absolute;left:216px;top:408px;width:214px;height:40px;
    background:var(--sky);transform:skewX(-12deg);
    border:1px solid #1a3a8c;
  }
  .uses-title{
    position:absolute;left:216px;top:408px;width:214px;height:40px;
    display:flex;align-items:center;justify-content:center;
    font-weight:700;font-style:italic;font-size:18px;text-shadow:0 1px 2px rgba(0,0,0,.35);
  }
  .uses-frame{position:absolute;left:0;top:0;width:1200px;height:626px;pointer-events:none}

  .uses{list-style:none}
  .use{position:absolute;top:472px;width:110px;margin-left:-55px;text-align:center;font-size:12px;line-height:14px}
  .use-icon{
    display:block;width:62px;height:62px;margin:0 auto 12px;border-radius:50%;
    background:radial-gradient(circle at 45% 40%, var(--white) 0%, var(--ice) 70%);
    border:3px solid var(--ring);box-shadow:2px 4px 6px rgba(0,0,0,.45);
  }

  .count{position:absolute;left:930px;top:488px;text-align:center;width:62px}
  .count-num{display:block;font-weight:300;font-size:54px;line-height:50px;letter-spacing:-2px}
  .count-unit{display:block;font-weight:300;font-size:17px;margin-top:4px}
  .size{position:absolute;left:1010px;top:504px;width:115px;text-align:center;font-weight:300;font-size:17px;line-height:21px}
</style>
</head>
<body>
<main class="label">
  <svg class="swoosh" viewBox="0 0 1200 626" aria-hidden="true">
    <defs>
      <linearGradient id="swooshFill" x1="0" y1="0" x2="0" y2="1">
        <stop offset="0" stop-color="#5a7ad0" stop-opacity=".6"/>
        <stop offset=".35" stop-color="#ffffff"/>
        <stop offset="1" stop-color="#ffffff"/>
      </linearGradient>
      <linearGradient id="swooshEdge" x1="0" y1="0" x2="0" y2="1">
        <stop offset="0" stop-color="#2a5fd0"/>
        <stop offset="1" stop-color="#1e8ae6"/>
      </linearGradient>
    </defs>
    <path d="M720 0 C 745 170, 710 320, 604 472 C 690 330, 760 170, 775 0 Z" fill="url(#swooshEdge)"/>
    <path d="M720 0 C 745 170, 710 320, 604 472 C 680 330, 740 170, 748 0 Z" fill="url(#swooshFill)"/>
  </svg>

  <div class="brand">
    <span class="brand-mark"></span>
    <span class="brand-name">Brisko Roll</span>
  </div>

  <ul class="features">
    <li class="feature f1">Perforated for Easy Tear</li>
    <li class="feature f2">Reusable</li>
    <li class="feature f3">Liquid Absorbent</li>
    <li class="feature f4">Non-Flammable</li>
    <li class="feature f5">Cadmium Free</li>
    <li class="feature f6">Kitchen Safe</li>
  </ul>

  <section class="facts">
    <h2 class="facts-title">Did you know?</h2>
    <p>
      <span class="line" style="left:793px;top:119px">Sponges are the perfect place for bacteria growth!</span>
      <span class="line" style="left:787px;top:142px">We're talking hundreds of different species of</span>
      <span class="line" style="left:778px;top:165px">bacteria growing in your dishwashing sponge - just</span>
      <span class="line" style="left:773px;top:188px">as bad as the inside of your toilet. So why use a dirty</span>
      <span class="line" style="left:763px;top:211px">sponge over and over again? Why does it smell so</span>
      <span class="line j" style="left:753px;top:235px">bad? Yes your toilet is gross, but why should the</span>
      <span class="line" style="left:744px;top:258px">sponge go overlooked?</span>
    </p>
    <p>
      <span class="line" style="left:730px;top:293px">The Brisko Roll is a sanitary solution to this problem.</span>
      <span class="line" style="left:720px;top:316px">Use it once, wash and reuse up to three times before</span>
      <span class="line" style="left:711px;top:339px">throwing each sheet away - that's enough for 180 washes</span>
      <span class="line" style="left:692px;top:362px">per roll! But don't limit yourself to dishwashing. It's great for</span>
      <span class="line" style="left:682px;top:386px">scrubbing surfaces with hardened debris or even dry residue</span>
      <span class="line" style="left:671px;top:409px">left from old spills. So go ahead, take a stand against bacteria and</span>
      <span class="line j" style="left:663px;top:432px">wash away knowing your kitchen is finally clean. Now that's</span>
      <span class="line" style="left:663px;top:455px">sanitary!</span>
    </p>
  </section>

  <svg class="uses-frame" viewBox="0 0 1200 626" aria-hidden="true">
    <path d="M60 472 V458 a10 10 0 0 1 10 -10 H188" fill="none" stroke="#c9d3ee" stroke-width="1"/>
    <path d="M442 448 H590 a10 10 0 0 1 10 10 V472" fill="none" stroke="#c9d3ee" stroke-width="1"/>
    <path d="M306 447 L316 465 L326 447 Z" fill="#4aa6dc"/>
  </svg>
  <div class="uses-tab" aria-hidden="true"></div>
  <h2 class="uses-title">Multipurpose Use</h2>

  <ul class="uses">
    <li class="use" style="left:112px"><span class="use-icon" role="img" aria-label="Sparkling plate icon"></span>Dishwashing</li>
    <li class="use" style="left:197px"><span class="use-icon" role="img" aria-label="Clean toilet icon"></span>Cleaning<br>Toilets</li>
    <li class="use" style="left:287px"><span class="use-icon" role="img" aria-label="Grill grate icon"></span>Cleaning<br>Grills</li>
    <li class="use" style="left:375px"><span class="use-icon" role="img" aria-label="Stove top icon"></span>Wiping<br>Down Stoves</li>
    <li class="use" style="left:460px"><span class="use-icon" role="img" aria-label="Sink basin icon"></span>Cleaning<br>Sinks</li>
    <li class="use" style="left:553px"><span class="use-icon" role="img" aria-label="Pet food bowl icon"></span>Cleaning<br>Pet Bowls</li>
  </ul>

  <div class="count"><span class="count-num">60</span><span class="count-unit">Sheets</span></div>
  <div class="size">7.9" X 8.7"<br>per sheet</div>
</main>
</body>
</html>
```